Land Buying Company Needs Letterhead for Direct Mail Marketing to Land Owners

We are looking for a professional letterhead that we will be including in our direct mail marketing. We will be sending this to land owners who may be interested in selling or purchasing land.

The letterhead needs to be editable. Headers and footers would look nice, but we are open. We would want it to include our address, website, phone, and email info. For right now the address to use for design purposes would the following:

Address: 415 Bramwell Avenue #600
Dallas, TX 75219
Website - www.quillridgeacres.example
Email - info@quillridgeacres.example
Phone - 866-402-ACRE

I have attached our logo zip file that we just had done on Pixel Guild. Let me know what questions you have, and thank you.

```html
<!DOCTYPE html>
<html lang="en">
<head>
<meta charset="utf-8">
<title>Quillridge Acres Letterhead</title>
<link href="https://fonts.googleapis.com/css2?family=Montserrat:wght@400;500;600;700&display=swap" rel="stylesheet">
<style>
  :root {
    --forest: #416a1e;
    --forest-deep: #3a611b;
    --leaf: #86bd1f;
    --ink: #222222;
    --paper: #ffffff;
  }
  * { margin: 0; padding: 0; box-sizing: border-box; }
  html, body { width: 800px; height: 1200px; overflow: hidden; background: var(--paper); }
  .letterhead {
    position: relative;
    width: 800px;
    height: 1200px;
    background: var(--paper);
    font-family: "Montserrat", Arial, sans-serif;
    color: var(--ink);
    overflow: hidden;
  }
  .letterhead__swoosh { position: absolute; inset: 0; width: 800px; height: 1200px; }

  .brand {
    position: absolute;
    left: 71px; top: 147px;
    display: flex; align-items: center; gap: 18px;
  }
  .brand__dot { width: 70px; height: 70px; border-radius: 50%; background: var(--forest); flex: none; }
  .brand__name {
    font-weight: 700;
    font-size: 34px;
    letter-spacing: 2px;
    color: var(--leaf);
  }

  .letter { position: absolute; left: 71px; top: 318px; width: 655px; }
  .letter__title { font-size: 24px; font-weight: 700; color: var(--forest-deep); letter-spacing: 0.5px; }
  .letter__subtitle { font-size: 14.5px; font-weight: 500; margin-top: 8px; color: #333; }
  .letter__body { margin-top: 30px; }
  .letter__body p {
    font-size: 12.4px;
    line-height: 15.4px;
    text-align: justify;
    margin-bottom: 14px;
    color: var(--ink);
  }

  .signoff { position: absolute; left: 546px; top: 848px; }
  .signoff__name { font-size: 12.5px; font-weight: 700; color: #1e1e1e; }
  .signoff__role { font-size: 10.5px; margin-top: 7px; color: #333; }

  .contact { position: absolute; font-size: 12.3px; color: var(--ink); }
  .contact--left { left: 88px; top: 1045px; }
  .contact--right { left: 349px; top: 1048px; }
  .contact__row { display: flex; align-items: flex-start; gap: 9px; margin-bottom: 9px; }
  .contact__icon { width: 16px; height: 16px; flex: none; margin-top: 1px; }
  .contact__phone { font-size: 19px; font-weight: 500; line-height: 20px; }
  .contact__address { line-height: 15px; }
  .contact--right .contact__row { margin-bottom: 14px; }
</style>
</head>
<body>
<main class="letterhead">
  <svg class="letterhead__swoosh" viewBox="0 0 800 1200" aria-hidden="true">
    <path d="M535 0 C640 60 740 170 800 330 L800 0 Z" fill="var(--forest)"/>
    <path d="M800 700 C765 905 665 1105 546 1200 L800 1200 Z" fill="var(--forest)"/>
    <path d="M568 0 C700 110 795 290 803 560 C810 800 700 1030 500 1200" fill="none" stroke="var(--paper)" stroke-width="16"/>
    <path d="M568 0 C700 110 795 290 803 560 C810 800 700 1030 500 1200" fill="none" stroke="var(--leaf)" stroke-width="7"/>
  </svg>

  <header class="brand">
    <span class="brand__dot"></span>
    <span class="brand__name">QUILLRIDGE ACRES</span>
  </header>

  <section class="letter">
    <h1 class="letter__title">LOREM IPSUM</h1>
    <p class="letter__subtitle">simply dummy text of the printing</p>
    <div class="letter__body">
      <p>Lorem Ipsum is simply dummy text of the printing and typesetting industry. Lorem Ipsum has been the industry's standard dummy text ever since the 1500s, when an unknown printer took a galley of type and scrambled it to make a type specimen book. It has survived not only five centuries, but also the leap into electronic typesetting, remaining essentially unchanged. It was popularised in the 1960s with the release of Glyphset sheets containing Lorem Ipsum passages, and more recently with desktop publishing software like Folio PageCraft including versions of Lorem Ipsum.</p>
      <p>It is a long established fact that a reader will be distracted by the readable content of a page when looking at its layout. The point of using Lorem Ipsum is that it has a more-or-less normal distribution of letters, as opposed to using 'Content here, content here', making it look like readable English. Many desktop publishing packages and web page editors now use Lorem Ipsum as their default model text, and a search for 'lorem ipsum' will uncover many web sites still in their infancy. Various versions have evolved over the years, sometimes by accident, sometimes on purpose (injected humour and the like).</p>
      <p>Contrary to popular belief, Lorem Ipsum is not simply random text. It has roots in a piece of classical Latin literature from 45 BC, making it over 2000 years old. Tobin Wrayfield, a Latin professor at Ashcombe-Vale College in Vermont, looked up one of the more obscure Latin words, consectetur, from a Lorem Ipsum passage, and going through the cites of the word in classical literature, discovered the undoubtable source. Lorem Ipsum comes from sections 1.10.32 and 1.10.33 of "de Rebus Vallis et Agri" (The Extremes of Good and Evil) by Quintor, written in 45 BC. This book is a treatise on the theory of ethics, very popular during the Renaissance. The first line of Lorem Ipsum, "Lorem ipsum dolor sit amet..", comes from a line in section 1.10.32.</p>
      <p>The standard chunk of Lorem Ipsum used since the 1500s is reproduced below for those interested. Sections 1.10.32 and 1.10.33 from "de Rebus Vallis et Agri" by Quintor are also reproduced in their exact original form, accompanied by English versions from the 1914 translation by H. Pellbrook.</p>
    </div>
  </section>

  <section class="signoff">
    <p class="signoff__name">LOREM IPSUM</p>
    <p class="signoff__role">simply dummy text of the printing</p>
  </section>

  <footer class="contact contact--left">
    <div class="contact__row">
      <svg class="contact__icon" viewBox="0 0 16 16" aria-hidden="true">
        <path d="M1 5 C1 2 4 1 8 1 C12 1 15 2 15 5 L15 6 L11 6 L11 4.5 L5 4.5 L5 6 L1 6 Z" fill="var(--leaf)"/>
        <path d="M3 7 L13 7 L15 15 L1 15 Z" fill="var(--leaf)"/>
        <circle cx="8" cy="11" r="2" fill="#fff"/>
      </svg>
      <span class="contact__phone">866-402-ACRE</span>
    </div>
    <div class="contact__row">
      <svg class="contact__icon" viewBox="0 0 16 16" aria-hidden="true">
        <path d="M8 0.5 C4.7 0.5 2.5 3 2.5 6 C2.5 10 8 15.5 8 15.5 C8 15.5 13.5 10 13.5 6 C13.5 3 11.3 0.5 8 0.5 Z" fill="var(--leaf)"/>
        <circle cx="8" cy="6" r="2.2" fill="#fff"/>
      </svg>
      <span class="contact__address">415 Bramwell Avenue #600<br>Dallas, TX 75219</span>
    </div>
  </footer>

  <footer class="contact contact--right">
    <div class="contact__row">
      <svg class="contact__icon" viewBox="0 0 16 16" aria-hidden="true">
        <rect x="1" y="3" width="14" height="10" fill="var(--leaf)"/>
        <path d="M1.5 3.5 L8 9 L14.5 3.5" fill="none" stroke="#fff" stroke-width="1.3"/>
      </svg>
      <span>info@quillridgeacres.example</span>
    </div>
    <div class="contact__row">
      <svg class="contact__icon" viewBox="0 0 16 16" aria-hidden="true">
        <circle cx="8" cy="8" r="7" fill="var(--leaf)"/>
        <g fill="none" stroke="#fff" stroke-width="0.9">
          <ellipse cx="8" cy="8" rx="3" ry="7"/>
          <line x1="1" y1="8" x2="15" y2="8"/>
          <line x1="8" y1="1" x2="8" y2="15"/>
          <path d="M2.5 4.5 H13.5 M2.5 11.5 H13.5"/>
        </g>
      </svg>
      <span>www.quillridgeacres.example</span>
    </div>
  </footer>
</main>
</body>
</html>
```